Poster design for the WILLOW WISP magic show.

We need a poster design for our magic show. This isn't your typical 'small town' magic show. Our show features world class magicians from the Velvet Lantern, in Hollywood California. The show is geared toward everyone, it is family friendly - with a little bit of an edge. We want people to see the poster and feel like they are going to have a unique and sophisticated magical experience. We also want individuals and couples to see the poster and feel like it is a show for them and not only for children.
Updates

Target Market(s)

BRT audience, family audience, the age range is anywhere from 5 - 105. Cool people.

Industry/Entity Type

Town

Requirements
Must have
• Our attached .jpg of the magician floating in the air. Poster size 24x36"
Must have text:
The 3rd Annual Albuquerque Conjuring Gala Presents (small type)
Willow Wisp (should be larger type)
November 24th - 25th
Showtimes 3:00PM & 7:30PM Saturday, 2:00PM Sunday
Tickets available at www.DorvaSeats.example For more information contact Dorva Theatre @ 505.555.0147
Nice to have
• A sort of old school/antique feeling to the poster.
Perhaps a theater marquee
Check out www.grovelumen.example - we love the feeling of this site for our poster...
Feel free to adjust the provided .jpg accordingly in regards to color/size/interaction with the rest of the poster
Should not have
• Should not have clowns, bunnies, anything that would make it feel like a 3 year old's magic themed birthday party.

```html
<!DOCTYPE html>
<html lang="en">
<head>
<meta charset="utf-8">
<title>Willow Wisp – Conjuring Gala Poster</title>
<link rel="stylesheet" href="https://fonts.googleapis.com/css2?family=Pinyon+Script&family=Rye&family=Sorts+Mill+Goudy&display=swap">
<style>
  :root {
    --olive: #b1ab61;
    --olive-dark: #6f6b31;
    --magenta: #b4189f;
    --ink: #1d140f;
    --title-light: #c9c25a;
    --title-dark: #3d3a10;
    --stage-red: #8e1a10;
    --stage-dark: #1a0806;
  }
  html, body {
    margin: 0;
    padding: 0;
    overflow: hidden;
    background: #222;
  }
  .poster {
    position: relative;
    width: 801px;
    height: 1200px;
    overflow: hidden;
    background: var(--olive);
  }
  .poster-art {
    position: absolute;
    inset: 0;
    display: block;
  }
  .presenter-line {
    position: absolute;
    top: 60px;
    left: 0;
    width: 801px;
    text-align: center;
    margin: 0;
    font-family: "Pinyon Script", cursive;
    font-weight: 400;
    font-size: 33px;
    color: var(--ink);
    letter-spacing: 0.3px;
    text-shadow: 0 0 1px var(--ink);
  }
  .show-title {
    position: absolute;
    top: 136px;
    left: 0;
    width: 801px;
    margin: 0;
    text-align: center;
    font-family: "Rye", serif;
    font-weight: 400;
    font-size: 62px;
    letter-spacing: 3px;
    color: var(--title-light);
    background: linear-gradient(180deg, #e0d86a 0%, #8b8420 55%, #3e3a0c 100%);
    -webkit-background-clip: text;
    background-clip: text;
    -webkit-text-fill-color: transparent;
    -webkit-text-stroke: 1.5px var(--title-dark);
  }
  .show-details {
    position: absolute;
    left: 35px;
    top: 824px;
    margin: 0;
    font-family: "Sorts Mill Goudy", serif;
    font-size: 18.5px;
    line-height: 27px;
    color: var(--ink);
  }
  .show-details p { margin: 0; }
  .dates { margin-bottom: 36px !important; }
  .showtime { padding-left: 43px; }
  .tickets { margin-top: 44px !important; }
  .contact { margin-top: 41px !important; }
</style>
</head>
<body>
<div class="poster">
  <svg class="poster-art" viewBox="0 0 979 1469" width="801" height="1200" preserveAspectRatio="none" aria-hidden="false">
    <defs>
      <filter id="grunge" x="0" y="0" width="100%" height="100%">
        <feTurbulence type="fractalNoise" baseFrequency="0.012" numOctaves="5" seed="7" result="noise"/>
        <feColorMatrix in="noise" type="matrix"
          values="0 0 0 0 0.27
                  0 0 0 0 0.26
                  0 0 0 0 0.10
                  0 0 0 2.6 -1.15"/>
      </filter>
      <filter id="speckle" x="0" y="0" width="100%" height="100%">
        <feTurbulence type="fractalNoise" baseFrequency="0.09" numOctaves="3" seed="3"/>
        <feColorMatrix type="matrix"
          values="0 0 0 0 0
                  0 0 0 0 0
                  0 0 0 0 0
                  0 0 0 1.6 -0.75"/>
      </filter>
      <radialGradient id="stageGlow" cx="0.5" cy="0.35" r="0.7">
        <stop offset="0" stop-color="var(--stage-red)"/>
        <stop offset="0.55" stop-color="#4a0f08"/>
        <stop offset="1" stop-color="var(--stage-dark)"/>
      </radialGradient>
    </defs>

    <!-- background texture -->
    <rect class="backdrop" width="979" height="1469" fill="var(--olive)"/>
    <rect class="backdrop-mottle" width="979" height="1469" filter="url(#grunge)"/>

    <!-- sunburst rays -->
    <g class="rays">
      <polygon fill="var(--magenta)" points="40,0 200,0 965,1445"/>
      <polygon fill="var(--ink)" points="235,0 335,0 965,1445"/>
      <polygon fill="var(--magenta)" points="515,0 612,0 965,1445"/>
      <polygon fill="var(--ink)" points="0,250 0,420 965,1445"/>
      <polygon fill="var(--magenta)" points="0,560 0,700 965,1445"/>
      <polygon fill="var(--ink)" points="388,0 430,0 965,1445"/>
    </g>
    <rect class="ray-wear" width="979" height="1469" filter="url(#speckle)" opacity="0.35"/>

    <!-- performer photograph frame -->
    <g class="photo-frame">
      <polygon points="80,368 865,305 912,835 113,905" fill="none" stroke="var(--ink)" stroke-width="4"/>
      <polygon points="84,376 858,322 898,848 116,892" fill="var(--magenta)"/>
      <polygon role="img" aria-label="Photograph of the magician floating above a chair on a red-lit stage"
        points="101,384 853,337 879,824 126,865" fill="url(#stageGlow)"/>
    </g>

    <!-- star trail -->
    <g class="star-trail" fill="var(--magenta)">
      <polygon points="250,1062 256,1080 275,1080 260,1091 266,1110 250,1098 234,1110 240,1091 225,1080 244,1080"/>
      <circle cx="262" cy="1120" r="4"/><circle cx="275" cy="1140" r="4"/>
      <circle cx="290" cy="1162" r="5"/><circle cx="302" cy="1186" r="4"/>
      <circle cx="320" cy="1210" r="5"/><circle cx="342" cy="1232" r="4"/>
      <circle cx="368" cy="1245" r="4"/><circle cx="398" cy="1250" r="4"/>
      <circle cx="430" cy="1248" r="4"/><circle cx="462" cy="1242" r="5"/>
      <circle cx="495" cy="1248" r="5"/><circle cx="520" cy="1268" r="4"/>
      <circle cx="538" cy="1292" r="4"/><circle cx="552" cy="1318" r="4"/>
      <circle cx="575" cy="1345" r="4"/><circle cx="600" cy="1365" r="4"/>
      <circle cx="630" cy="1378" r="3"/><circle cx="660" cy="1384" r="3"/>
    </g>
    <line class="wand" x1="692" y1="1386" x2="960" y2="1440" stroke="var(--ink)" stroke-width="20" stroke-linecap="round"/>
  </svg>

  <h2 class="presenter-line">The 3rd Annual Albuquerque Conjuring Gala Presents</h2>
  <h1 class="show-title">WILLOW&nbsp;&nbsp;WISP</h1>

  <div class="show-details">
    <p class="dates">November 24th - 25th</p>
    <p>Showtimes:</p>
    <p class="showtime">3:00PM &amp; 7:30PM Saturday,</p>
    <p class="showtime">2:00PM Sunday</p>
    <p class="tickets">Tickets available at www.DorvaSeats.example</p>
    <p class="contact">For more information contact Dorva Theatre @ 505.555.0147</p>
  </div>
</div>
</body>
</html>
```